Building Servicess

We need a new business card design for a company. We specialise in: Electrical/Site temporary electrics, Data/Network Installation, Passive Fire Protection

Industry/Entity Type

Construction

Contact Information for Business Card

Services provided as detailed on project description

Font styles to use
Serif

Colors
0054AA
0677BA
7BADD7
CADEEF
E8F1F8
00AB8E
00BBA5
67D7C9
C6EFE9
E9F9F6
EB3D1F
EC4F4E
F09395
F8D3D4
FCEDEE

Requirements
Must have
• Company logo-contact details-phone numbers

```html
<!DOCTYPE html>
<html lang="en">
<head>
<meta charset="utf-8">
<title>Northgate Site Services – Business Card</title>
<link href="https://fonts.googleapis.com/css2?family=Lora:wght@700&family=Lato:wght@400;700&display=swap" rel="stylesheet">
<style>
  :root {
    --backdrop: #b2b2b2;
    --card-white: #ffffff;
    --brand-blue: #0f76bc;
    --brand-grey: #808185;
    --ink: #1a1a1a;
    --title-ink: #333333;
  }
  * { margin: 0; padding: 0; box-sizing: border-box; }
  html, body { width: 1200px; height: 1200px; overflow: hidden; }
  body {
    background: var(--backdrop);
    position: relative;
    font-family: "Lato", sans-serif;
  }
  .card {
    position: absolute;
    left: 239px;
    width: 722px;
    height: 412px;
  }
  .card-front { top: 171px; background: var(--card-white); }
  .card-back { top: 616px; background: var(--brand-blue); }

  .company-mark {
    position: absolute;
    left: 27px;
    top: 136px;
    width: 316px;
    display: flex;
    flex-direction: column;
    align-items: center;
    gap: 14px;
    color: var(--brand-blue);
    font-family: "Lato", sans-serif;
    font-weight: 700;
    text-align: center;
  }
  .company-mark .mark-square {
    width: 70px; height: 70px;
    background: var(--brand-blue);
  }
  .company-mark .mark-name {
    font-size: 25px;
    letter-spacing: 0.5px;
    line-height: 1.15;
    text-transform: uppercase;
  }

  .holder {
    position: absolute;
    right: 33px;
    top: 98px;
    text-align: right;
  }
  .holder-name {
    font-family: "Lora", serif;
    font-weight: 700;
    font-size: 30px;
    line-height: 1;
  }
  .holder-name .first { color: var(--brand-blue); }
  .holder-name .last { color: var(--brand-grey); }
  .holder-title {
    margin-top: 6px;
    font-size: 17px;
    color: var(--title-ink);
    letter-spacing: 0.2px;
  }

  .contact-icons {
    position: absolute;
    right: 32px;
    top: 208px;
    display: flex;
    gap: 7px;
  }
  .contact-icons svg { width: 19px; height: 19px; display: block; }

  .contact-list {
    position: absolute;
    right: 32px;
    top: 256px;
    list-style: none;
    text-align: right;
    color: var(--ink);
    font-size: 17px;
  }
  .contact-list li { height: 31px; line-height: 22px; }
  .contact-list .contact-web { font-size: 16.5px; }
  .contact-list .contact-mail { font-size: 16.5px; }

  .back-name {
    position: absolute;
    inset: 0;
    display: flex;
    align-items: center;
    justify-content: center;
    color: var(--card-white);
    font-family: "Lato", sans-serif;
    font-weight: 700;
    font-size: 34px;
    letter-spacing: 1px;
    text-transform: uppercase;
  }
</style>
</head>
<body>
  <section class="card card-front">
    <div class="company-mark">
      <span class="mark-square"></span>
      <span class="mark-name">Northgate Site Services Ltd</span>
    </div>

    <div class="holder">
      <h1 class="holder-name"><span class="first">Tomas</span> <span class="last">Brenner</span></h1>
      <p class="holder-title">MANAGING DIRECTOR</p>
    </div>

    <div class="contact-icons">
      <svg viewBox="0 0 20 20" aria-label="Office phone">
        <circle cx="10" cy="10" r="10" fill="var(--brand-blue)"/>
        <path d="M4.5 8.5 Q10 4.5 15.5 8.5 L14.5 10 L12.5 9.3 L12.3 8 Q10 7.3 7.7 8 L7.5 9.3 L5.5 10 Z" fill="#fff"/>
        <rect x="6.5" y="10.5" width="7" height="4.5" rx="0.8" fill="#fff"/>
      </svg>
      <svg viewBox="0 0 20 20" aria-label="Mobile phone">
        <circle cx="10" cy="10" r="10" fill="var(--brand-blue)"/>
        <path d="M6.2 4.8 L8.2 4.6 L9.1 7.4 L7.8 8.4 Q8.9 10.9 11.4 12.2 L12.5 10.9 L15.2 11.9 L15 13.9 Q13.8 15.4 11.5 14.6 Q6.3 12.3 5.2 7.2 Q5 5.6 6.2 4.8 Z" fill="#fff"/>
      </svg>
      <svg viewBox="0 0 20 20" aria-label="Email">
        <circle cx="10" cy="10" r="10" fill="var(--brand-blue)"/>
        <path d="M4.5 9.8 L15.2 5 L12.6 15 L9.8 11.6 L13.3 7.3 L8.6 10.8 Z" fill="#fff"/>
      </svg>
      <svg viewBox="0 0 20 20" aria-label="Website">
        <circle cx="10" cy="10" r="10" fill="var(--brand-blue)"/>
        <g fill="none" stroke="#fff" stroke-width="1.6" stroke-linecap="round">
          <path d="M9 11 L11 9"/>
          <path d="M8.2 9.4 L6.6 11 A2 2 0 0 0 9.4 13.8 L11 12.2"/>
          <path d="M11.8 10.6 L13.4 9 A2 2 0 0 0 10.6 6.2 L9 7.8"/>
        </g>
      </svg>
    </div>

    <ul class="contact-list">
      <li class="contact-phone">020 79460958</li>
      <li class="contact-phone">077 00900461</li>
      <li class="contact-mail">tomasbrenner@mailbox.com</li>
      <li class="contact-web">www.tomasbrenner.com</li>
    </ul>
  </section>

  <section class="card card-back">
    <div class="back-name">Northgate</div>
  </section>
</body>
</html>
```